We need a business card design, letterhead design and envelope design for our corporate image

We are looking for a corporate business card design, letterhead and envelope design to match the business card design. Logo is done.

```html
<!DOCTYPE html>
<html lang="en">
<head>
<meta charset="utf-8">
<title>Verolan Stationery Set</title>
<link rel="stylesheet" href="https://fonts.googleapis.com/css2?family=Montserrat:ital,wght@0,300;0,400;0,500;0,700;0,800;1,300&display=swap">
<style>
  :root {
    --backdrop: #ffc84a;
    --paper: #ffffff;
    --brand-yellow: #f7c400;
    --flap-light: #eab800;
    --flap-dark: #c79500;
    --ink: #3c3c3c;
    --ink-soft: #8a8a8a;
  }
  * { box-sizing: border-box; margin: 0; padding: 0; }
  html, body { width: 1200px; height: 502px; overflow: hidden; }
  body {
    position: relative;
    background: var(--backdrop);
    font-family: "Montserrat", sans-serif;
    color: var(--ink);
  }

  /* brand lockup */
  .brand {
    display: flex;
    align-items: center;
    gap: 7px;
    font-family: "Montserrat", sans-serif;
    font-weight: 700;
    color: var(--ink);
    line-height: 1;
  }
  .brand-dot {
    background: var(--brand-yellow);
    border-radius: 50%;
    flex: none;
  }

  /* letterhead */
  .letterhead {
    position: absolute;
    left: 39px; top: 30px;
    width: 308px; height: 434px;
    background: var(--paper);
  }
  .letterhead .brand { position: absolute; left: 0; right: 0; top: 34px; justify-content: center; font-size: 22px; }
  .letterhead .brand-dot { width: 12px; height: 12px; }
  .sender-name {
    position: absolute; left: 22px; top: 96px;
    font-size: 12.5px; font-weight: 800; color: var(--brand-yellow);
  }
  .sender-role {
    position: absolute; left: 22px; top: 112px;
    font-size: 9px; font-weight: 300; color: var(--ink-soft);
  }
  .letter-date {
    position: absolute; right: 23px; top: 115px;
    font-size: 6.5px; font-weight: 300; color: var(--ink-soft);
  }
  .letter-body {
    position: absolute; left: 21px; right: 21px; top: 136px;
    font-size: 6.2px; font-weight: 300; line-height: 14.2px;
    color: var(--ink-soft); text-align: justify;
  }
  .signature {
    position: absolute; left: 204px; top: 343px;
    width: 77px; height: 24px;
    background: linear-gradient(90deg, #f2f2f2, #e4e4e4);
    border-radius: 3px;
  }
  .signature-name {
    position: absolute; left: 215px; top: 380px;
    font-size: 7.5px; font-style: italic; font-weight: 300; color: var(--ink-soft);
  }
  .letter-footer {
    position: absolute; left: 0; right: 0; bottom: 0; height: 20px;
    background: var(--brand-yellow);
    display: flex; align-items: center; justify-content: space-around;
    padding: 0 10px;
    font-size: 8px; color: var(--paper);
  }
  .letter-footer span { display: flex; align-items: center; gap: 4px; }

  /* business cards */
  .card {
    position: absolute;
    left: 430px; width: 277px; height: 158px;
    background: var(--paper);
    border-radius: 16px;
  }
  .card-front { top: 83px; }
  .card-front .brand { position: absolute; left: 0; right: 0; top: 66px; justify-content: center; font-size: 25px; }
  .card-front .brand-dot { width: 13px; height: 13px; }
  .card-back { top: 276px; }
  .holder-name {
    position: absolute; left: 19px; top: 66px;
    font-size: 15px; font-weight: 700; color: var(--brand-yellow); letter-spacing: 0.3px;
  }
  .holder-role {
    position: absolute; left: 19px; top: 84px;
    font-size: 9px; font-weight: 400; color: var(--ink); letter-spacing: 0.6px;
  }
  .card-contacts {
    position: absolute; left: 168px; top: 61px;
    list-style: none; font-size: 5.8px; font-weight: 400; color: var(--ink);
  }
  .card-contacts li { display: flex; align-items: center; gap: 5px; height: 9.8px; }
  .card-contacts svg { flex: none; }

  /* envelopes */
  .envelope-back {
    position: absolute; left: 788px; top: 83px;
    width: 369px; height: 179px;
  }
  .envelope-front {
    position: absolute; left: 788px; top: 288px;
    width: 369px; height: 144px;
    background: var(--paper);
  }
  .envelope-front .brand { position: absolute; left: 19px; top: 104px; font-size: 16px; gap: 5px; }
  .envelope-front .brand-dot { width: 9px; height: 9px; }
  .address-window {
    position: absolute; left: 230px; top: 77px;
    width: 102px; height: 45px; border-radius: 3px;
    background: linear-gradient(120deg, #cfcfcf, #eeeeee 55%, #d6d6d6);
  }
</style>
</head>
<body>

  <article class="letterhead">
    <div class="brand"><span class="brand-dot"></span>Verolan</div>
    <h2 class="sender-name">NAME SURNAME</h2>
    <p class="sender-role">MANAGER</p>
    <p class="letter-date">Dec. 28, 2021</p>
    <div class="letter-body">
      <p>Lorem ipsum dolor sit amet, consectetuer adipiscing elit, sed diam nonummy nibh euismod tincidunt ut laoreet dolore magna aliquam erat volutpat. Ut wisi enim ad minim veniam, quis nostrud exerci tation ullamcorper suscipit lobortis nisl ut aliquip ex ea commodo consequat. qui blandit praesent luptatum zzril delenit augue duis dolore te feugait nulla facilisi.</p>
      <p>Lorem ipsum dolor sit amet, cons ectetuer adipiscing elit, sed diam nonummy nibh euismod tincidunt ut laoreet dolore magna aliquam erat volutpat. Ut wisi enim ad minim veniam, quis nostrud exerci tation ullamcorper suscipit lobortis nisl ut aliquip ex ea commodo consequat.</p>
      <p>Lorem ipsum dolor sit amet, consectetuer adipiscing elit, sed diam nonummy nibh euismod tincidunt ut laoreet dolore magna aliquam erat volutpat. Ut wisi enim ad minim veniam,vel illum dolore eu feugiat nulla facilisis at vero eros et accumsan et iusto odio dignissim qui blandit praesent luptatum zzril delenit augue duis dolore te feugait nulla facilisi.</p>
    </div>
    <div class="signature" role="img" aria-label="Handwritten signature"></div>
    <p class="signature-name">LOREM IPSUM</p>
    <footer class="letter-footer">
      <span>
        <svg width="8" height="6" viewBox="0 0 8 6"><rect width="8" height="6" rx="0.8" fill="#fff"/><path d="M0.5 0.6 L4 3.4 L7.5 0.6" stroke="#f7c400" stroke-width="0.8" fill="none"/></svg>
        info@verolan-mail.com
      </span>
      <span>
        <svg width="7" height="7" viewBox="0 0 10 10"><path d="M2 0.5 L4 3 L3 4.2 Q4.5 6 5.8 7 L7 6 L9.5 8 L8 9.6 Q4 9 0.5 2 Z" fill="#fff"/></svg>
        +0100 555 20 417
      </span>
      <span>
        <svg width="8" height="8" viewBox="0 0 10 10" fill="none" stroke="#fff" stroke-width="0.9"><circle cx="5" cy="5" r="4.3"/><ellipse cx="5" cy="5" rx="1.9" ry="4.3"/><path d="M0.7 5 H9.3"/></svg>
        www.verolan.com
      </span>
    </footer>
  </article>

  <section class="card card-front">
    <div class="brand"><span class="brand-dot"></span>Verolan</div>
  </section>

  <section class="card card-back">
    <h2 class="holder-name">DARA PELLIN</h2>
    <p class="holder-role">GRAPHIC DESIGNER</p>
    <ul class="card-contacts">
      <li><svg width="6" height="6" viewBox="0 0 10 10"><path d="M5 0.5 L9.5 5 H8 V9.5 H2 V5 H0.5 Z" fill="#f7c400"/></svg>48, Harbor Lane 12</li>
      <li><svg width="6" height="6" viewBox="0 0 10 10"><path d="M2 0.5 L4 3 L3 4.2 Q4.5 6 5.8 7 L7 6 L9.5 8 L8 9.6 Q4 9 0.5 2 Z" fill="#f7c400"/></svg>00 555 2047</li>
      <li><svg width="6" height="6" viewBox="0 0 10 10"><rect y="2" width="10" height="6.5" rx="0.8" fill="#f7c400"/></svg>info@verolan-mail.com</li>
      <li><svg width="6" height="6" viewBox="0 0 10 10"><circle cx="5" cy="5" r="4.8" fill="#f7c400"/><path d="M0.5 5 H9.5 M5 0.3 V9.7" stroke="#fff" stroke-width="0.8"/></svg>www.verolan.com</li>
    </ul>
  </section>

  <svg class="envelope-back" viewBox="0 0 369 179" aria-hidden="true">
    <defs>
      <linearGradient id="flap-fill" x1="0" y1="0" x2="0" y2="1">
        <stop offset="0" stop-color="#eab800"/>
        <stop offset="1" stop-color="#c79500"/>
      </linearGradient>
    </defs>
    <rect x="0" y="35" width="369" height="144" fill="#ffffff"/>
    <polygon points="20,0 349,0 369,35 0,35" fill="url(#flap-fill)"/>
    <polygon points="0,35 353,35 333,69 47,69" fill="#f7c400"/>
  </svg>

  <section class="envelope-front">
    <div class="brand"><span class="brand-dot"></span>Verolan</div>
    <div class="address-window"></div>
  </section>

</body>
</html>
```